Printed Circuit Board Company Web Site Design - Please see new file 82012 web design

We are a printed circuit board manufacturer. Need a company professional web site to allow our potential customers to know more about our background, capability and our products. The web site will contain three languages, which are Chinese, English and Japanese. Our audience are mainly electronic companies that procure printed circuit boards. I have a word document that have all the required text in all three languages. The final design should communicate the impression that we embrace quality, trustworthiness and long term partnership business principles.
We should have sections that allow us to post pictures of our facilities.
I have added the three files in three different languages.
Some of the information is below:
Background
RVT Global Limited (RVT) was set up in Hong Kong in 2007 by two Hong Kong entrepreneurs, Mr. Lau Fong and Mr. Tak Wai. We acquired the single sided printed circuit board factory located in Dongguan City, Guangdong Province, China, from Bolvane Corporation of the U.S. in 2007. In addition to RVT, Mr. Fong and Mr. Wai also own Harbor Dynamics Company Limited, a semiconductor company based in Hong Kong since 1997 with a total investment of over US$100 million. Harbor is engaged in the manufacturing of flexible substrates and MEMS assembly business.
RVT has been awarded TS 16949 and ISO14000 certificates since 2009 and 2004 respectively.
Business Principles
RVT Global Limited strives to be a professional top notched printed circuit board supplier. We embrace four “EXCELLENCE” principles, namely, excellence in quality, excellence in prices, excellence in services and excellence in on time delivery.
We approach each customer with a long-term partnership view that delivers the lowest ownership costs and highest total values to our customers. We customize quotations and solutions in order to allow our customers to win more businesses. We believe by thinking from our customers’ points of view we will be able to create a WIN-WIN relationship.
Customers
Due to our excellent quality, services and production systems, RVT Global Limited manage to service a number of large Japanese and US customers, which include:
Technical capability overview
Below is an overview of our current capability:
Target Market(s)
Electronic companies buyers
Industry/Entity Type
Business
Requirements
Must have
- Capability description
Should not have
- no cartoon

```html
<!DOCTYPE html>
<html lang="en">
<head>
<meta charset="utf-8">
<title>RVT Global Limited</title>
<link href="https://fonts.googleapis.com/css2?family=Roboto+Condensed:wght@400;700&display=swap" rel="stylesheet">
<style>
:root{
  --green:#0b6b3e;
  --green-dark:#084f2e;
  --bg:#eeeeee;
  --bar:#d2d2d2;
  --panel:#c9c9c9;
  --text:#555;
  --nav-text:#666;
  --white:#fff;
  --accent:#ffd200;
}
*{margin:0;padding:0;box-sizing:border-box}
html,body{width:1200px;height:707px;overflow:hidden}
body{background:linear-gradient(180deg,#f3f3f3,#e8e8e8);font-family:"Roboto Condensed",sans-serif;color:var(--text);position:relative}
.brand{position:absolute;left:236px;top:28px;color:var(--green);font-weight:700;line-height:1}
.brand-name{font-size:50px;letter-spacing:14px}
.brand-sub{font-size:18px;letter-spacing:3px;margin-top:2px;padding-left:10px}
.contact{position:absolute;left:850px;font-size:15px;color:#777;display:flex;align-items:center;gap:12px}
.contact svg{width:18px;height:16px}
.contact.phone{top:31px}
.contact.mail{top:58px}
.nav{position:absolute;left:234px;top:110px;width:782px;height:40px;background:linear-gradient(#dcdcdc,#c6c6c6);border-radius:6px;display:flex;align-items:center;box-shadow:0 1px 2px rgba(0,0,0,.2)}
.nav a{font-size:14px;color:var(--nav-text);text-decoration:none;text-transform:uppercase;padding:0 11px}
.nav a.active{background:linear-gradient(#1b8a52,var(--green-dark));color:var(--white);height:40px;line-height:40px;width:62px;text-align:center;border-radius:6px 0 0 6px;margin-right:3px}
.hero{position:absolute;left:236px;top:158px;width:778px;height:266px;background:var(--white);padding:2px;box-shadow:0 1px 3px rgba(0,0,0,.3)}
.hero-photo{position:relative;width:100%;height:100%;background:linear-gradient(100deg,#cfd2d4 0%,#b9bcbd 40%,#9fa3a3 70%,#a8735a 95%)}
.hero-caption{position:absolute;left:0;right:0;bottom:0;height:76px;background:rgba(50,50,50,.75);padding:8px 14px;color:var(--white)}
.hero-title{font-size:22px;text-transform:uppercase}
.hero-title em{font-style:normal;color:var(--accent)}
.hero-lines{font-size:9px;font-weight:700;line-height:16px;margin-top:3px;padding-left:3px}
.content{position:absolute;left:236px;top:424px;width:778px;height:234px;background:var(--panel);border-radius:0 0 8px 8px}
.card{position:absolute;top:16px;width:242px;height:204px;background:var(--white);border-radius:0 0 8px 8px;overflow:hidden}
.card-head{position:relative;height:52px}
.card-head svg{position:absolute;inset:0}
.card-title{position:relative;color:var(--white);font-size:11px;padding:9px 8px;text-transform:uppercase;letter-spacing:.3px}
.card ul{list-style:none;font-size:10.5px;padding:16px 13px 0 13px;line-height:18.6px;text-transform:uppercase;letter-spacing:.3px}
.card li{display:flex}
.card li span:first-child{width:132px;flex:none}
.more{position:absolute;right:0;bottom:0;width:30px;height:25px;background:var(--green);color:var(--white);font-size:22px;font-weight:700;line-height:25px;text-align:center}
.footer{position:absolute;left:236px;top:664px;width:778px;height:40px;background:linear-gradient(#d8d8d8,#c8c8c8);border-radius:6px;padding:6px 14px}
.footer-brand{font-size:14px;font-weight:700;color:#777;letter-spacing:4px}
.footer-rights{font-size:9px;color:#666;margin-top:2px}
.footer-links{position:absolute;right:16px;top:15px;font-size:9px;display:flex;gap:12px}
.footer-links a{color:#666;text-decoration:none}
</style>
</head>
<body>
<header>
  <div class="brand"><div class="brand-name">RVT</div><div class="brand-sub">Global Limited</div></div>
  <div class="contact phone"><svg viewBox="0 0 18 16"><path d="M1 6c2-4 14-4 16 0l-3 2-2-2v-1H6v1L4 8z" fill="#888"/><rect x="4" y="9" width="10" height="6" rx="1" fill="#888"/></svg>+91 900 555 0142</div>
  <div class="contact mail"><svg viewBox="0 0 18 16"><rect x="1" y="2" width="16" height="12" fill="#999"/><path d="M1 2l8 7 8-7" stroke="#fff" fill="none"/></svg>info@rvtglobal.com</div>
</header>
<nav class="nav">
  <a class="active" href="#">Home</a><a href="#">Printed Circuit Boards</a><a href="#">Support &amp; Resources</a><a href="#">About Us</a><a href="#">Knowledge Center</a><a href="#">Contact Us</a><a href="#">Get A Quote</a>
</nav>
<section class="hero">
  <div class="hero-photo" role="img" aria-label="Photo of the circuit board production line with processing machines">
    <div class="hero-caption">
      <div class="hero-title">Lorem ipsum <em>dolor</em> sit amet</div>
      <div class="hero-lines">LOREM IPSUM DOLOR SIT AMET &nbsp;LOREM IPSUM DOLOR<br>LOREM IPSUM DOLOR SIT AMET &nbsp;LOREM IPSUM DOLORT AMET</div>
    </div>
  </div>
</section>
<main class="content">
  <article class="card" style="left:14px">
    <div class="card-head"><svg width="242" height="52" viewBox="0 0 242 52" preserveAspectRatio="none"><path d="M0 0H242V25C140 25 40 30 0 52Z" fill="#0b6b3e"/></svg><div class="card-title">Raw Materials</div></div>
    <ul>
      <li><span>Paper Phenolic</span><span>XPC, FR-1 &amp; FR-2</span></li>
      <li><span>Paper Epoxy</span><span>CEM-1</span></li>
      <li><span>Glass Epoxy</span><span>CEM-3 &amp; FR-4</span></li>
      <li><span>Overall Thickness (T)</span><span>0.4mm - 1.6mm ± 0.13mm depend on customer</span></li>
    </ul>
    <div class="more">+</div>
  </article>
  <article class="card" style="left:267px">
    <div class="card-head"><svg width="242" height="52" viewBox="0 0 242 52" preserveAspectRatio="none"><path d="M0 0H242V25C140 25 40 30 0 52Z" fill="#0b6b3e"/></svg><div class="card-title">Printing Processes</div></div>
    <ul style="padding-left:17px">
      <li>Screen Printing</li><li>Minimum Track Width (W</li><li>Minimum Line Spacing (W)</li><li>Pattern Registration</li><li>Minimum of Annular Ring</li><li>Etching</li>
    </ul>
    <div class="more">+</div>
  </article>
  <article class="card" style="left:521px">
    <div class="card-head"><svg width="242" height="52" viewBox="0 0 242 52" preserveAspectRatio="none"><path d="M0 0H242V25C140 25 40 30 0 52Z" fill="#0b6b3e"/></svg><div class="card-title">Punching and CNC Process</div></div>
    <ul style="padding-left:18px">
      <li>Outline Dimension</li><li>Hole Position Accuracy</li><li>Hole Diameter Accuracy</li><li>Minimum Punching Hole Size</li><li>Minimum Rectangular Slot Size</li><li>Min. Distance Between Two Slots</li>
    </ul>
    <div class="more">+</div>
  </article>
</main>
<footer class="footer">
  <div class="footer-brand">RVT</div>
  <div class="footer-rights">ALL RIGHTS RESERVED @ RVTGLOBAL.COM</div>
  <div class="footer-links"><a href="#">HOME</a><a href="#">CONTACT US</a><a href="#">ABOUT US</a><a href="#">PRIVACY POLICY</a><a href="#">TERMS</a></div>
</footer>
</body>
</html>
```